creating a certificate for our flagship course

Hi,
We need a new certificate for our flagship course called Rising Tide. We have been running this course for 25 years this year and want to get something special that represents that. We need our logos incorporated and we love to have a compass or Koru incorporated in the certificate. We like something different from your standard certificate, but not too crazy.

The text should say something along the lines of:
This certificate is awarded to ....
For successfully completing and contributing to the three day Rising Tide programme.

signed:... date:...

to learn a bit more about this course and our company, please check our website. www.veldonmarstik.co.nz

Thank you!

attendees who completed our 3 day programme.

• Both our RT logo and our brand logo. a compass or a koru.
• a 25th year existence something on it.

```html
<!DOCTYPE html>
<html lang="en">
<head>
<meta charset="utf-8">
<title>Rising Tide — Certificate of Completion</title>
<link rel="stylesheet" href="https://fonts.googleapis.com/css2?family=Open+Sans:ital,wght@0,400;0,600;0,700;1,400;1,700&display=swap">
<style>
  :root {
    --backdrop: #bdbec0;
    --paper: #ffffff;
    --green-deep: #23891c;
    --green-name: #3c9a2a;
    --green-band: #3f9629;
    --green-mid: #8dbe78;
    --green-pale: #c7ddc3;
    --green-faint: #d6efd4;
    --ink: #1a1a1a;
    --ink-soft: #3c4248;
    --brand-dark: #2d2d3f;
    --brand-square: #8bc34a;
  }
  * { margin: 0; padding: 0; box-sizing: border-box; }
  html, body {
    width: 1200px;
    height: 1000px;
    overflow: hidden;
    background: var(--backdrop);
    font-family: "Open Sans", Arial, sans-serif;
  }
  .certificate {
    position: absolute;
    left: 82px;
    top: 112px;
    width: 1031px;
    height: 796px;
    background: var(--paper);
    overflow: hidden;
  }
  .decor {
    position: absolute;
    inset: 0;
    width: 1031px;
    height: 796px;
  }
  .title {
    position: absolute;
    left: 60px;
    top: 106px;
    color: var(--green-deep);
    font-weight: 700;
    line-height: 1;
  }
  .title__main {
    display: block;
    font-size: 66px;
    letter-spacing: -1px;
  }
  .title__sub {
    display: block;
    margin-top: 6px;
    font-size: 25px;
    letter-spacing: -0.3px;
  }
  .award {
    position: absolute;
    left: 124px;
    top: 288px;
    height: 207px;
    border-left: 3px solid var(--green-deep);
    padding-left: 43px;
  }
  .award__intro {
    margin-top: 1px;
    font-style: italic;
    font-size: 20px;
    color: var(--ink);
    letter-spacing: -0.3px;
  }
  .award__name {
    margin-top: 41px;
    font-weight: 700;
    font-size: 33px;
    color: var(--green-name);
    letter-spacing: -0.2px;
  }
  .award__reason {
    margin-top: 30px;
    font-style: italic;
    font-size: 16.5px;
    line-height: 23px;
    color: var(--ink);
    letter-spacing: -0.3px;
    margin-left: 3px;
  }
  .sign-field {
    position: absolute;
    top: 617px;
    width: 150px;
    border-top: 2px solid var(--green-deep);
    text-align: center;
    padding-top: 4px;
    font-style: italic;
    font-weight: 700;
    font-size: 14px;
    color: var(--ink);
  }
  .sign-field--date { left: 176px; }
  .sign-field--signature { left: 489px; }
  .company {
    position: absolute;
    left: 630px;
    top: 88px;
    display: flex;
    align-items: center;
    gap: 15px;
  }
  .company__square {
    width: 55px;
    height: 55px;
    background: var(--brand-dark);
  }
  .company__name {
    font-size: 22px;
    font-weight: 400;
    line-height: 24px;
    color: var(--brand-dark);
    letter-spacing: 0.5px;
  }
  .programme {
    position: absolute;
    left: 800px;
    top: 708px;
    display: flex;
    align-items: center;
    gap: 10px;
  }
  .programme__square {
    width: 50px;
    height: 50px;
    background: var(--brand-square);
  }
  .programme__name {
    font-size: 20px;
    font-weight: 400;
    color: var(--ink-soft);
  }
</style>
</head>
<body>
  <main class="certificate">
    <svg class="decor" viewBox="0 0 1031 796" aria-hidden="false">
      <defs>
        <radialGradient id="compass-glow" cx="50%" cy="50%" r="50%">
          <stop offset="0%" stop-color="var(--green-faint)" stop-opacity="0.9"/>
          <stop offset="70%" stop-color="var(--green-faint)" stop-opacity="0.55"/>
          <stop offset="100%" stop-color="var(--green-faint)" stop-opacity="0"/>
        </radialGradient>
      </defs>
      <circle class="decor__compass" cx="861" cy="331" r="320" fill="url(#compass-glow)" role="img" aria-label="Faint compass rose decoration"/>
      <path class="decor__pale" fill="var(--green-pale)" d="M560 796 C 800 700, 960 560, 1031 300 L1031 796 Z"/>
      <path class="decor__mid" fill="var(--green-mid)" d="M0 750 C 350 790, 820 750, 1031 300 L1031 420 C 950 630, 780 750, 560 796 L0 796 Z"/>
      <path class="decor__band" fill="var(--green-band)" d="M150 768 C 560 792, 920 640, 1031 160 L1031 320 C 930 620, 640 780, 150 768 Z"/>
    </svg>

    <header class="company">
      <span class="company__square"></span>
      <span class="company__name">VELDON<br>MARSTIK &amp; Associates</span>
    </header>

    <h1 class="title">
      <span class="title__main">CERTIFICATE</span>
      <span class="title__sub">OF COMPLETION</span>
    </h1>

    <section class="award">
      <p class="award__intro">This certificate is awarded to</p>
      <p class="award__name">AMELIA HARTLEY</p>
      <p class="award__reason">For successfully completing and contributing to the three day<br>Rising Tide programme.</p>
    </section>

    <div class="sign-field sign-field--date">Date</div>
    <div class="sign-field sign-field--signature">Signature</div>

    <footer class="programme">
      <span class="programme__square"></span>
      <span class="programme__name">Rising Tide</span>
    </footer>
  </main>
</body>
</html>
```